Top of the line business card design needed for real estate brokerage

We currently have a business card with our logo but would like to have a revised version. We would love for you to implement your own design that will catch anyone's attention. The theme colors should be black, royal blue, gray/silver, and white.The contact information should be the same as the info on our current business card (picture attached). In the design that we pick, we will need to be able to edit the text so that we can customize the text content for each of our agents. Same goes for the professional picture. There should be an area on the card that each agent can have their professional portrait attached. Please include a version without the picture option as well for agents that do not wish to have a professional picture attached.

```html
<!DOCTYPE html>
<html lang="en">
<head>
<meta charset="utf-8">
<title>Clearstone Realty – Business Card</title>
<link href="https://fonts.googleapis.com/css2?family=Open+Sans:wght@400;600;700&display=swap" rel="stylesheet">
<style>
  :root {
    --royal-blue: #1f5bb5;
    --ink: #1b1b1b;
    --silver: #9a9a9a;
    --silver-light: #d9d9d9;
    --paper: #ffffff;
    --backdrop: #ececec;
    --body-text: #333333;
  }
  * { box-sizing: border-box; margin: 0; padding: 0; }
  html, body {
    width: 1200px; height: 900px; overflow: hidden;
    background: var(--backdrop);
    font-family: "Open Sans", Arial, sans-serif;
  }
  .canvas {
    position: relative; width: 1200px; height: 900px;
  }
  .card {
    position: absolute; width: 560px; height: 320px;
    background: var(--paper);
    box-shadow: 0 6px 18px rgba(0,0,0,0.12);
    overflow: hidden;
  }
  .card--back { left: 560px; top: 90px; }
  .card--front { left: 80px; top: 490px; }

  /* Back */
  .skyline {
    position: absolute; left: 0; top: 0; width: 100%; height: 100%;
    background: linear-gradient(180deg, #f4f4f4 0%, #e2e2e2 60%, #f4f4f4 100%);
  }
  .service-band {
    position: absolute; left: 0; top: 140px; width: 100%; height: 86px;
    background: var(--royal-blue);
    padding: 16px 28px;
    color: var(--paper);
    font-size: 15px; line-height: 26px; letter-spacing: 0.2px;
  }
  .service-band .divider { margin: 0 8px; }
  .back-brand {
    position: absolute; left: 0; top: 84px; width: 100%;
    display: flex; justify-content: center; align-items: center; gap: 10px;
  }
  .brand-name {
    font-weight: 700; color: var(--royal-blue);
    font-size: 26px; letter-spacing: 0.5px;
  }
  .brand-mark {
    width: 18px; height: 18px; background: var(--royal-blue);
  }
  .back-brand .brand-name { color: var(--ink); }
  .back-brand .brand-mark { background: var(--ink); }

  /* Front */
  .agent {
    position: absolute; left: 34px; top: 32px;
  }
  .agent-name {
    color: var(--royal-blue); font-weight: 700; font-size: 17px;
  }
  .agent-title {
    color: var(--body-text); font-size: 11px; margin-top: 1px;
  }
  .contact {
    position: absolute; left: 34px; top: 100px;
    color: var(--body-text); font-size: 12.5px; line-height: 18px;
  }
  .contact .address { margin-bottom: 6px; }
  .contact-line { display: flex; align-items: center; gap: 7px; }
  .contact-line svg { width: 10px; height: 10px; flex: none; }
  .front-brand {
    position: absolute; right: 34px; top: 188px;
    display: flex; align-items: center; gap: 10px;
  }
  .website {
    position: absolute; right: 34px; bottom: 30px;
    color: var(--royal-blue); font-size: 14px;
  }
</style>
</head>
<body>
<main class="canvas">

  <section class="card card--back" aria-label="Card back">
    <div class="skyline" role="img" aria-label="Line drawing of a city skyline in light gray"></div>
    <div class="back-brand">
      <span class="brand-mark"></span>
      <span class="brand-name">Clearstone Realty</span>
    </div>
    <div class="service-band">
      <p>Residential Real Estate<span class="divider">|</span>Commercial Real Estate</p>
      <p>Property Management<span class="divider">|</span>Investments</p>
    </div>
  </section>

  <section class="card card--front" aria-label="Card front">
    <div class="agent">
      <p class="agent-name">Daniel Avery</p>
      <p class="agent-title">Broker</p>
    </div>
    <div class="contact">
      <p class="address">2100 Harbor View Dr Suite 310<br>Lake Palms, FL 33400</p>
      <p class="contact-line">
        <svg viewBox="0 0 10 10"><rect x="2" y="0.5" width="6" height="9" rx="1" fill="none" stroke="#1f5bb5" stroke-width="1.2"/></svg>
        555-210-4387
      </p>
      <p class="contact-line">
        <svg viewBox="0 0 10 10"><rect x="0.5" y="2" width="9" height="7" rx="1" fill="#1f5bb5"/><rect x="2" y="0.5" width="6" height="2" fill="#1f5bb5"/></svg>
        555-210-4390
      </p>
      <p class="contact-line">
        <svg viewBox="0 0 10 10"><rect x="0.5" y="3" width="9" height="6" fill="#1f5bb5"/><rect x="2.5" y="0.5" width="5" height="3" fill="none" stroke="#1f5bb5"/></svg>
        555-318-0622
      </p>
      <p class="contact-line">
        <svg viewBox="0 0 10 10"><rect x="0.5" y="2" width="9" height="6.5" fill="none" stroke="#1f5bb5"/><path d="M0.5 2 L5 6 L9.5 2" fill="none" stroke="#1f5bb5"/></svg>
        daniel@clearstonerealty.com
      </p>
    </div>
    <div class="front-brand">
      <span class="brand-mark"></span>
      <span class="brand-name">Clearstone Realty</span>
    </div>
    <p class="website">www.clearstonerealty.com</p>
  </section>

</main>
</body>
</html>
```